zenRate Flash Banner Ad

We require a flash banner ad for a new product of ours called zenRate (www.zenrate.com.au). zenRate is a web-based system generating life insurance quotes using a widget embedded in your site.
The banner should have the following screens:
1. Life Insurance, Total & Permanent Disablement Insurance, Income Protection Insurance
2. No Blood Tests or Medicals Required.
3. Up to $1 million Cover with Leading Brands.
4. Click here for an Instant Quote.
We require the following sizes:
- 300 x 250
- 728 x 90
Industry/Entity Type
Life Insurance
Look and feel
Each slider illustrates characteristics of the customer's brand and the style your logo design should communicate.

```html
<!DOCTYPE html>
<html lang="en">
<head>
<meta charset="utf-8">
<title>zenRate Banner Colourways</title>
<link rel="stylesheet" href="https://fonts.googleapis.com/css2?family=Archivo+Black&family=Arimo:ital,wght@0,400;0,700;1,400;1,700&display=swap">
<style>
  :root {
    --canvas: #ffffff;
    --ink: #111111;
    --white: #ffffff;
    --floor-light: #f6e3cf;
    --floor-dark: #e6c3a0;
    --brand-grey: #7a7a7a;
    --brand-green: #5cbf3a;
    --cta-fill: rgba(0, 0, 0, 0.55);
    --photo-light: rgba(255, 255, 255, 0.55);
    --photo-soft: rgba(255, 255, 255, 0.12);
    --red: #b3120f;
    --red-hi: #d2302a;
    --teal: #2f8f9c;
    --teal-hi: #55b4bf;
    --purple: #9a55b8;
    --purple-hi: #c287dc;
    --green: #2f8a45;
    --green-hi: #5cb86c;
    --grey: #5c5c5c;
    --grey-hi: #8d8d8d;
  }
  * { box-sizing: border-box; margin: 0; padding: 0; }
  html, body { width: 1200px; height: 900px; overflow: hidden; background: var(--canvas); }
  body { position: relative; font-family: "Arimo", Arial, sans-serif; }

  .banner {
    position: absolute;
    width: 340px;
    height: 283px;
    overflow: hidden;
    border: 1px solid #333;
    background: radial-gradient(ellipse at 45% 40%, var(--hi) 0%, var(--base) 75%);
    transform-origin: top left;
  }
  .banner--red    { --base: var(--red);    --hi: var(--red-hi);    left: 48px;  top: 97px; transform: scale(0.9735); }
  .banner--teal   { --base: var(--teal);   --hi: var(--teal-hi);   left: 433px; top: 97px; }
  .banner--purple { --base: var(--purple); --hi: var(--purple-hi); left: 817px; top: 97px; }
  .banner--green  { --base: var(--green);  --hi: var(--green-hi);  left: 180px; top: 481px; }
  .banner--grey   { --base: var(--grey);   --hi: var(--grey-hi);   left: 675px; top: 481px; }

  .banner__floor {
    position: absolute; left: 0; right: 0; top: 203px; bottom: 0;
    background: linear-gradient(180deg, var(--floor-light), var(--floor-dark));
  }
  .banner__photo {
    position: absolute; left: 270px; top: 0; width: 70px; height: 203px;
    background: linear-gradient(90deg, var(--photo-soft), var(--photo-light));
  }
  .banner__lead {
    position: absolute; left: 22px; top: 20px;
    font-style: italic; font-weight: 700; font-size: 21px; color: var(--ink);
  }
  .banner__headline {
    position: absolute; left: 20px; top: 46px;
    font-style: italic; font-weight: 700; font-size: 23px; color: var(--white);
    letter-spacing: 0.3px; white-space: nowrap;
  }
  .banner__products {
    position: absolute; left: 22px; top: 86px; list-style: none;
    font-size: 14px; color: var(--ink); line-height: 22px;
  }
  .banner__products li { display: flex; align-items: center; gap: 7px; }
  .banner__products svg { width: 14px; height: 12px; flex: none; }
  .banner__products b {
    font-family: "Archivo Black", "Arial Black", sans-serif; font-weight: 400;
    font-style: italic; letter-spacing: 1.2px;
  }
  .banner__products i { letter-spacing: 0.8px; }
  .banner__cta {
    position: absolute; left: 69px; top: 161px; width: 128px; height: 30px;
    display: flex; align-items: center; justify-content: center;
    background: var(--cta-fill); border: 1.5px solid var(--white); border-radius: 6px;
    color: var(--white); text-decoration: none;
    font-style: italic; font-weight: 700; font-size: 16px;
  }
  .banner__powered {
    position: absolute; left: 10px; top: 210px;
    font-size: 11px; color: #5a4a3a;
  }
  .banner__brand {
    position: absolute; left: 16px; top: 234px;
    display: flex; align-items: center; gap: 8px;
    font-size: 27px; color: var(--brand-grey);
  }
  .banner__brand-dot {
    width: 36px; height: 36px; border-radius: 50%; background: var(--brand-green);
  }
</style>
</head>
<body>

<article class="banner banner--red">
  <div class="banner__floor"></div>
  <div class="banner__photo" role="img" aria-label="Photo of a woman in white lying on the floor with legs raised against the wall, beneath a small house sketch"></div>
  <p class="banner__lead">For An</p>
  <h2 class="banner__headline">INSTANT QUOTE ON</h2>
  <ul class="banner__products">
    <li><svg viewBox="0 0 14 12"><path d="M0 4h7V0l7 6-7 6V8H0z" fill="#fff"/></svg><b>LIFE</b><i>Insurance</i></li>
    <li><svg viewBox="0 0 14 12"><path d="M0 4h7V0l7 6-7 6V8H0z" fill="#fff"/></svg><b>TPD</b><i>Insurance</i></li>
    <li><svg viewBox="0 0 14 12"><path d="M0 4h7V0l7 6-7 6V8H0z" fill="#fff"/></svg><b>INCOME</b><i>Protection</i></li>
  </ul>
  <a class="banner__cta" href="#">CLICK HERE</a>
  <p class="banner__powered">Powered by</p>
  <div class="banner__brand"><span class="banner__brand-dot"></span>covernest</div>
</article>

<article class="banner banner--teal">
  <div class="banner__floor"></div>
  <div class="banner__photo" role="img" aria-label="Photo of a woman in white lying on the floor with legs raised against the wall, beneath a small house sketch"></div>
  <p class="banner__lead">For An</p>
  <h2 class="banner__headline">INSTANT QUOTE ON</h2>
  <ul class="banner__products">
    <li><svg viewBox="0 0 14 12"><path d="M0 4h7V0l7 6-7 6V8H0z" fill="#fff"/></svg><b>LIFE</b><i>Insurance</i></li>
    <li><svg viewBox="0 0 14 12"><path d="M0 4h7V0l7 6-7 6V8H0z" fill="#fff"/></svg><b>TPD</b><i>Insurance</i></li>
    <li><svg viewBox="0 0 14 12"><path d="M0 4h7V0l7 6-7 6V8H0z" fill="#fff"/></svg><b>INCOME</b><i>Protection</i></li>
  </ul>
  <a class="banner__cta" href="#">CLICK HERE</a>
  <p class="banner__powered">Powered by</p>
  <div class="banner__brand"><span class="banner__brand-dot"></span>covernest</div>
</article>

<article class="banner banner--purple">
  <div class="banner__floor"></div>
  <div class="banner__photo" role="img" aria-label="Photo of a woman in white lying on the floor with legs raised against the wall, beneath a small house sketch"></div>
  <p class="banner__lead">For An</p>
  <h2 class="banner__headline">INSTANT QUOTE ON</h2>
  <ul class="banner__products">
    <li><svg viewBox="0 0 14 12"><path d="M0 4h7V0l7 6-7 6V8H0z" fill="#fff"/></svg><b>LIFE</b><i>Insurance</i></li>
    <li><svg viewBox="0 0 14 12"><path d="M0 4h7V0l7 6-7 6V8H0z" fill="#fff"/></svg><b>TPD</b><i>Insurance</i></li>
    <li><svg viewBox="0 0 14 12"><path d="M0 4h7V0l7 6-7 6V8H0z" fill="#fff"/></svg><b>INCOME</b><i>Protection</i></li>
  </ul>
  <a class="banner__cta" href="#">CLICK HERE</a>
  <p class="banner__powered">Powered by</p>
  <div class="banner__brand"><span class="banner__brand-dot"></span>covernest</div>
</article>

<article class="banner banner--green">
  <div class="banner__floor"></div>
  <div class="banner__photo" role="img" aria-label="Photo of a woman in white lying on the floor with legs raised against the wall, beneath a small house sketch"></div>
  <p class="banner__lead">For An</p>
  <h2 class="banner__headline">INSTANT QUOTE ON</h2>
  <ul class="banner__products">
    <li><svg viewBox="0 0 14 12"><path d="M0 4h7V0l7 6-7 6V8H0z" fill="#fff"/></svg><b>LIFE</b><i>Insurance</i></li>
    <li><svg viewBox="0 0 14 12"><path d="M0 4h7V0l7 6-7 6V8H0z" fill="#fff"/></svg><b>TPD</b><i>Insurance</i></li>
    <li><svg viewBox="0 0 14 12"><path d="M0 4h7V0l7 6-7 6V8H0z" fill="#fff"/></svg><b>INCOME</b><i>Protection</i></li>
  </ul>
  <a class="banner__cta" href="#">CLICK HERE</a>
  <p class="banner__powered">Powered by</p>
  <div class="banner__brand"><span class="banner__brand-dot"></span>covernest</div>
</article>

<article class="banner banner--grey">
  <div class="banner__floor"></div>
  <div class="banner__photo" role="img" aria-label="Photo of a woman in white lying on the floor with legs raised against the wall, beneath a small house sketch"></div>
  <p class="banner__lead">For An</p>
  <h2 class="banner__headline">INSTANT QUOTE ON</h2>
  <ul class="banner__products">
    <li><svg viewBox="0 0 14 12"><path d="M0 4h7V0l7 6-7 6V8H0z" fill="#fff"/></svg><b>LIFE</b><i>Insurance</i></li>
    <li><svg viewBox="0 0 14 12"><path d="M0 4h7V0l7 6-7 6V8H0z" fill="#fff"/></svg><b>TPD</b><i>Insurance</i></li>
    <li><svg viewBox="0 0 14 12"><path d="M0 4h7V0l7 6-7 6V8H0z" fill="#fff"/></svg><b>INCOME</b><i>Protection</i></li>
  </ul>
  <a class="banner__cta" href="#">CLICK HERE</a>
  <p class="banner__powered">Powered by</p>
  <div class="banner__brand"><span class="banner__brand-dot"></span>covernest</div>
</article>

</body>
</html>
```